Desserts Business Card Design

I own a dessert business and cakes and cupcakes are my biggest sellers. I have been running this as a part time business since 2007. I am now looking to expand going full time and open a store front within he next 12 months.
With this expansion I am looking to have my own design setup for the business.

I have been using a design on my cards provided to me by a website I got the cards from. I would like a more original design I can use for the cards, the store front and any other advertising I will be doing. I also have a saying on the back of my business card which I would like to be worked in as well.
"Every sweet is baked by hand, with love"

Target Market(s)

Younger and older families of all ethnic backgrounds

Industry/Entity Type

Advertising

Contact Information for Business Card

Maribel's Sugarcraft Sweets
Dorian Pike
4372 Halloway Crscent
Oshawa, Ontario
L3T 8N4

Logo Text

Logo styles of interest
Emblem Logo
Pictorial/Combination Logo
Wordmark Logo
Lettermark Logo
Requirements
Must have
• "Every sweet is baked by hand, with love"
Nice to have
• Maribel's Sugarcraft Sweets - This can actually be turned into a logo which is really what I am looking for. Using MSS, converted to a logo? I am really looking to see what you can provide me with.
A cake or cupcake added on the front of the card?
Should not have
• I cannot think of anything right now. I an looking forward to see the imaginations from the design groups

```html
<!DOCTYPE html>
<html lang="en">
<head>
<meta charset="utf-8">
<title>Maribel's Sugarcraft Sweets – Business Card</title>
<link rel="stylesheet" href="https://fonts.googleapis.com/css2?family=Damion&family=Oswald:wght@500&display=swap">
<style>
  :root {
    --canvas: #ececec;
    --pink: #f5aacd;
    --pink-text: #f0a6c8;
    --white: #ffffff;
    --wood-light: #b0702a;
    --wood-mid: #7a4716;
    --wood-dark: #3c220b;
    --ink: #222222;
  }
  * { box-sizing: border-box; margin: 0; padding: 0; }
  html, body { width: 1200px; height: 1000px; overflow: hidden; }
  body {
    position: relative;
    background: radial-gradient(ellipse at 55% 35%, #f7f7f7 0%, var(--canvas) 70%, #dcdcdc 100%);
    font-family: "Damion", cursive;
  }

  /* Brand presentation */
  .brand-sheet {
    position: absolute; left: 690px; top: 95px; width: 460px;
    text-align: center; color: var(--pink-text);
  }
  .brand-sheet .brand-dot {
    width: 230px; height: 230px; border-radius: 50%;
    background: var(--pink); margin: 0 auto 22px;
  }
  .brand-sheet .brand-name { font-size: 38px; line-height: 1; white-space: nowrap; }
  .brand-sheet .tagline { font-size: 16px; margin-top: 4px; padding-left: 150px; white-space: nowrap; }

  /* Card front */
  .card { position: absolute; width: 560px; height: 320px; box-shadow: 0 8px 18px rgba(0,0,0,.35); }
  .card-front { left: 50px; top: 300px; overflow: hidden; }
  .card-front .wood {
    position: absolute; inset: 0;
    background:
      repeating-linear-gradient(90deg, rgba(0,0,0,.28) 0 2px, transparent 2px 46px),
      radial-gradient(ellipse at 50% 40%, var(--wood-light) 0%, var(--wood-mid) 55%, var(--wood-dark) 100%);
  }
  .card-front .front-content {
    position: absolute; inset: 0; text-align: center; color: var(--pink-text);
  }
  .card-front .brand-dot {
    width: 150px; height: 150px; border-radius: 50%;
    background: var(--pink); margin: 34px auto 14px;
  }
  .card-front .brand-name { font-size: 34px; line-height: 1; white-space: nowrap; }
  .card-front .tagline { font-size: 14px; padding-left: 150px; margin-top: 2px; white-space: nowrap; }

  /* Card back */
  .card-back { left: 560px; top: 585px; width: 600px; height: 340px; background: var(--pink); color: var(--white); }
  .card-back .brand-dot {
    position: absolute; left: 44px; top: 48px;
    width: 150px; height: 150px; border-radius: 50%; background: var(--white);
  }
  .card-back .person { position: absolute; left: 240px; top: 44px; font-size: 30px; }
  .card-back .contact-list { position: absolute; left: 240px; top: 98px; list-style: none; font-size: 18px; }
  .card-back .contact-list li { display: flex; align-items: center; gap: 10px; height: 30px; white-space: nowrap; }
  .card-back .contact-list svg { width: 18px; height: 18px; fill: var(--white); flex: none; }
  .card-back .address { position: absolute; left: 90px; bottom: 44px; font-size: 19px; letter-spacing: .3px; white-space: nowrap; }

  /* Colour swatch */
  .swatch { position: absolute; left: 100px; top: 884px; display: flex; align-items: center; gap: 26px; }
  .swatch .chip { width: 84px; height: 82px; background: var(--pink); }
  .swatch .code { font-family: "Oswald", sans-serif; font-weight: 500; font-size: 40px; color: var(--ink); }
</style>
</head>
<body>

  <section class="brand-sheet">
    <div class="brand-dot"></div>
    <p class="brand-name">Maribel's Sugarcraft Sweets</p>
    <p class="tagline">Every sweet is baked by hand, with love</p>
  </section>

  <section class="card card-front">
    <div class="wood" role="img" aria-label="Dark wooden plank texture background"></div>
    <div class="front-content">
      <div class="brand-dot"></div>
      <p class="brand-name">Maribel's Sugarcraft Sweets</p>
      <p class="tagline">Every sweet is baked by hand, with love</p>
    </div>
  </section>

  <section class="card card-back">
    <div class="brand-dot"></div>
    <p class="person">Dorian Pike</p>
    <ul class="contact-list">
      <li><svg viewBox="0 0 24 24" aria-hidden="true"><path d="M6.6 10.8a15 15 0 0 0 6.6 6.6l2.2-2.2a1 1 0 0 1 1-.25 11.4 11.4 0 0 0 3.6.57 1 1 0 0 1 1 1V20a1 1 0 0 1-1 1A17 17 0 0 1 3 4a1 1 0 0 1 1-1h3.5a1 1 0 0 1 1 1c0 1.25.2 2.45.57 3.570a1 1 0 0 1-.25 1z"/></svg>289-555-0147</li>
      <li><svg viewBox="0 0 24 24" aria-hidden="true"><path d="M2 5h20v14H2zm2 2v.5l8 5 8-5V7zm0 2.8V17h16V9.8l-8 5z"/></svg>hello.treats@maribelssweets.com</li>
      <li><svg viewBox="0 0 24 24" aria-hidden="true"><path d="M12 3 2 12h3v9h6v-6h2v6h6v-9h3z"/></svg>www.maribelssweets.com</li>
    </ul>
    <p class="address">4372 Halloway Crscent Oshawa, Ontario L3T 8N4</p>
  </section>

  <div class="swatch">
    <div class="chip"></div>
    <span class="code">M40</span>
  </div>

</body>
</html>
```